Broadway Haulage website

We need a website design for a towing company based in Australia.
The design should be simple and minimalist. The site can be in colours of the logo are Blue, Red and White (see attached) - but we'd like to see options in some sort of industrial looking metallic theme if possible.
We base our business on our friendly and efficient customer service, the design should attempt to convey this in some way.

Industry/Entity Type

Industrial

Font styles to use
Sans Serif

```html
<!DOCTYPE html>
<html lang="en">
<head>
<meta charset="utf-8">
<title>Broadway Haulage</title>
<link href="https://fonts.googleapis.com/css2?family=Open+Sans:wght@400;600;700;800&display=swap" rel="stylesheet">
<style>
:root{
  --red:#d3201f;
  --red-dark:#a8140f;
  --ink:#222;
  --dark:#1d1d1d;
  --darker:#141414;
  --grey-bg:#e9e9e9;
  --card:#ffffff;
  --muted:#888;
  --line:#d6d6d6;
  --navy:#1b3a7a;
}
*{box-sizing:border-box;margin:0;padding:0}
html,body{width:724px;height:1200px;overflow:hidden}
body{font-family:"Open Sans",Arial,sans-serif;color:var(--ink);background:#fff;position:relative}

/* header */
.topbar{height:42px;background:var(--darker);padding:6px 22px;color:#ddd;display:flex;justify-content:space-between}
.topbar .phone{font-size:13px;font-weight:700;color:#fff;line-height:16px}
.topbar .email{font-size:9px;color:#aaa}
.search{width:118px;height:18px;background:#2e2e2e;border:1px solid #444;font-size:8px;color:#888;padding:3px 6px;margin-top:4px;position:relative}
.search svg{position:absolute;right:4px;top:3px}
.nav{height:30px;background:linear-gradient(#de2b27,var(--red-dark));display:flex;align-items:center;padding:0 22px;position:relative;z-index:2}
.nav a{color:#fff;font-size:9px;font-weight:700;text-decoration:none;margin-right:22px;text-transform:uppercase}
.nav .spacer{flex:1}
.brand{position:absolute;left:50%;top:-42px;transform:translateX(-50%);width:86px;height:92px;background:#fff;box-shadow:0 2px 6px rgba(0,0,0,.35);display:flex;flex-direction:column;align-items:center;justify-content:center;z-index:3}
.brand .mark{width:30px;height:30px;background:var(--navy);border-radius:50%;margin-bottom:6px}
.brand .name{font-size:8px;font-weight:800;color:var(--navy);text-transform:uppercase;text-align:center;line-height:10px}

/* hero */
.hero{height:322px;background:linear-gradient(180deg,#9aa3ab 0%,#c4c9cc 45%,#5f6468 62%,#3f4244 100%);position:relative}
.arrow{position:absolute;top:140px;width:18px;height:30px;background:rgba(0,0,0,.55);display:flex;align-items:center;justify-content:center}
.arrow.left{left:0}.arrow.right{right:0}

/* services */
.services{background:var(--grey-bg);padding:96px 78px 24px;height:430px}
.grid{display:grid;grid-template-columns:repeat(3,1fr);gap:20px 16px}
.card{background:var(--card);height:152px;text-align:center;padding:14px 14px 0;box-shadow:0 1px 2px rgba(0,0,0,.12)}
.icon{width:36px;height:36px;border-radius:50%;background:#3a3a3a;margin:0 auto 10px;display:flex;align-items:center;justify-content:center}
.card h3{font-size:11px;font-weight:800;text-transform:uppercase;margin-bottom:6px}
.card p{font-size:7px;color:var(--muted);line-height:10px;margin-bottom:8px}
.btn{display:inline-block;background:#555;color:#fff;font-size:7px;padding:3px 10px;border-radius:2px}

/* welcome */
.welcome{padding:26px 60px 0;text-align:center;height:150px}
.welcome h2{font-size:14px;font-weight:800;text-transform:uppercase;margin-bottom:12px}
.welcome h2 span{color:var(--red)}
.welcome p{font-size:7px;color:var(--muted);line-height:10px;margin-bottom:8px}

/* footer */
.footer{position:absolute;left:0;top:984px;width:724px;height:216px;background:var(--dark);color:#ccc}
.cols{display:flex;padding:22px 72px 0;gap:22px;height:180px}
.col h4{font-size:10px;font-weight:700;color:#fff;text-transform:uppercase;margin-bottom:10px}
.testi{width:230px}
.bubble{background:#3a3a3a;padding:10px;font-size:7px;line-height:10px;color:#bbb;position:relative}
.bubble:after{content:"";position:absolute;left:14px;bottom:-8px;border:8px solid transparent;border-top-color:#3a3a3a;border-bottom:0}
.client{margin-top:14px;font-size:8px;color:#fff}
.client small{display:block;font-size:7px;color:#999}
.contact{width:140px;border-left:1px solid #333;padding-left:12px}
.row{display:flex;gap:6px;font-size:7px;line-height:10px;color:#aaa;margin-bottom:10px}
.row svg{flex:none}
.social{width:170px;border-left:1px solid #333;padding-left:12px}
.squares{display:flex;gap:4px;margin-bottom:16px}
.squares i{width:18px;height:18px;display:block}
.links{font-size:7px;color:#aaa;line-height:12px}
.copy{height:36px;border-top:1px solid #333;text-align:center;font-size:7px;color:#888;line-height:36px}
</style>
</head>
<body>
<header>
  <div class="topbar">
    <div><div class="phone">(800) 555 0142</div><div class="email">info@broadwayhaulage.com</div></div>
    <div class="search">Enter Your Search
      <svg width="9" height="9" viewBox="0 0 10 10"><circle cx="4" cy="4" r="3" fill="none" stroke="#999" stroke-width="1.4"/><line x1="6.3" y1="6.3" x2="9" y2="9" stroke="#999" stroke-width="1.4"/></svg>
    </div>
  </div>
  <nav class="nav">
    <a>Home</a><a>About Us</a><a>Services</a><a>News</a>
    <span class="spacer"></span>
    <a>Our Team</a><a>Testimonials</a><a style="margin-right:0">Contact</a>
    <div class="brand"><div class="mark"></div><div class="name">Broadway<br>Haulage</div></div>
  </nav>
</header>

<section class="hero" role="img" aria-label="Photo of a white flatbed tow truck carrying a van on a road">
  <div class="arrow left"><svg width="8" height="12"><polyline points="6,1 2,6 6,11" fill="none" stroke="#fff" stroke-width="2"/></svg></div>
  <div class="arrow right"><svg width="8" height="12"><polyline points="2,1 6,6 2,11" fill="none" stroke="#fff" stroke-width="2"/></svg></div>
</section>

<section class="services">
  <div class="grid">
    <div class="card"><div class="icon"><svg width="20" height="14" viewBox="0 0 20 14"><path d="M2 8l2-5h12l2 5v4H2z" fill="#fff"/><circle cx="6" cy="12" r="2" fill="#3a3a3a"/><circle cx="14" cy="12" r="2" fill="#3a3a3a"/></svg></div>
      <h3>Vehicle Delivery</h3><p>We move your vehicle safely to any address in town. Our drivers handle every job with care and keep you informed along the way.</p><span class="btn">Read More</span></div>
    <div class="card"><div class="icon"><svg width="18" height="18" viewBox="0 0 18 18"><path d="M3 15l7-7M10 8a4 4 0 1 0 3-5l-2 2 2 2 2-2a4 4 0 0 1-5 3" fill="none" stroke="#fff" stroke-width="2"/></svg></div>
      <h3>Car Recovery</h3><p>Broken down or stuck in a ditch? Our crew arrives fast with the right gear to recover your car and get you back on the road.</p><span class="btn">Read More</span></div>
    <div class="card"><div class="icon"><svg width="20" height="14" viewBox="0 0 20 14"><rect x="1" y="2" width="11" height="8" fill="#fff"/><path d="M12 5h4l3 3v2h-7z" fill="#fff"/><circle cx="5" cy="12" r="2" fill="#fff"/><circle cx="15" cy="12" r="2" fill="#fff"/></svg></div>
      <h3>Transportation</h3><p>Long distance or local, we carry cars, vans and light trucks across the state on modern flatbeds with full insurance cover.</p><span class="btn">Read More</span></div>
    <div class="card"><div class="icon"><svg width="18" height="18" viewBox="0 0 18 18"><path d="M6 2L3 16M12 2l3 14" stroke="#fff" stroke-width="2"/><path d="M9 3v2M9 8v2M9 13v2" stroke="#fff" stroke-width="1.6"/></svg></div>
      <h3>Road Side Assistance</h3><p>Flat tyre, empty tank or dead battery, help is one call away. We are on duty day and night to keep you moving safely.</p><span class="btn">Read More</span></div>
    <div class="card"><div class="icon"><svg width="18" height="18" viewBox="0 0 18 18"><circle cx="9" cy="9" r="5" fill="none" stroke="#fff" stroke-width="3" stroke-dasharray="3 2"/><circle cx="9" cy="9" r="2" fill="#fff"/></svg></div>
      <h3>Equipment Hauling</h3><p>Heavy machines, trailers and site gear are loaded and secured by trained staff, then delivered on time to your work site.</p><span class="btn">Read More</span></div>
    <div class="card"><div class="icon"><svg width="18" height="18" viewBox="0 0 18 18"><path d="M2 6l7-4 7 4v8l-7 3-7-3z" fill="#fff"/><path d="M2 6l7 3 7-3M9 9v8" stroke="#3a3a3a" stroke-width="1"/></svg></div>
      <h3>Relocation</h3><p>Moving house or office? We relocate your vehicles and bulky items with the same friendly and efficient service you expect.</p><span class="btn">Read More</span></div>
  </div>
</section>

<section class="welcome">
  <h2>Welcome to <span>Broadway Haulage</span></h2>
  <p>We are a family owned towing business serving drivers across Australia. Our team is friendly, quick and fully licensed, with a modern fleet ready around the clock for any job, large or small, near or far.</p>
  <p>From a simple jump start to moving heavy plant, we treat every customer like a neighbour. Clear prices, honest advice and fast arrival times are the reasons people call us again and again and tell their friends.</p>
</section>

<footer class="footer">
  <div class="cols">
    <div class="col testi"><h4>Testimonials</h4>
      <div class="bubble">They came within twenty minutes and towed my car to the workshop. The driver was kind, the price was fair and I would call them again without thinking twice.</div>
      <div class="client">- Client's Name<small>Happy driver, Sydney</small></div></div>
    <div class="col contact"><h4>Contact Details</h4>
      <div class="row"><svg width="9" height="11" viewBox="0 0 9 11"><path d="M4.5 0a4 4 0 0 0-4 4c0 3 4 7 4 7s4-4 4-7a4 4 0 0 0-4-4z" fill="#d3201f"/></svg><span>12 Harbour Road, Unit 4<br>Port City NSW 2000</span></div>
      <div class="row"><svg width="9" height="11" viewBox="0 0 9 11"><path d="M1 1h3l1 3-2 1a6 6 0 0 0 3 3l1-2 3 1v3a9 9 0 0 1-9-9z" fill="#d3201f"/></svg><span>Phone:<br>(800) 555 0142</span></div>
      <div class="row"><svg width="10" height="8" viewBox="0 0 10 8"><rect width="10" height="8" fill="#d3201f"/><polyline points="0,0 5,4 10,0" fill="none" stroke="#1d1d1d"/></svg><span>Email:<br>info@broadwayhaulage.com</span></div></div>
    <div class="col social"><h4>Stay Connected</h4>
      <div class="squares"><i style="background:#3b5998"></i><i style="background:#1da1f2"></i><i style="background:#0077b5"></i><i style="background:#dd4b39"></i><i style="background:#c4302b"></i><i style="background:#888"></i></div>
      <h4>Quick Links</h4>
      <div class="links">Home | About Us | Services | News<br>Our Team | Testimonials | Contact</div></div>
  </div>
  <div class="copy">Copyright 2014 Broadway Haulage. All Rights Reserved.</div>
</footer>
</body>
</html>
```